We need to design Labels of one of Our Brand BrivaLune Lotion.

The purpose of this product is to keep mosquitoes away.
There are 3 variants of this lotion. So we need 3 designs for the product. These variants details are mentioned below:

1) Mosquito Repellent Lotion with Lavender Fragrance.
2) Mosquito Repellent Lotion with Natural Ingredients.
3) Mosquito Repellent Lotion for kids.

Kindly note the bottle will be WHITE for all the variants. Cap will of the bottle will be with accordance to the color of label. In the picture it is red just for presentation.

Kindly share design of Repellent Lotion with Lavendar Fragrance initially and if we give your positive feedback, then you may add further variants of the design.

The bottle shape is attached along with keylines. Also attaching logo. If there is any other option for logo, you can suggest which we would probably keep our existing logo.

Target Market(s)

B+, B, C+

Industry/Entity Type

Product

Colors
a54499
6b449b

Requirements
Must have
• Mosquito
• 100ml
Nice to have
• Purple color as background
Should not have
• Lavendar flower

```html
<!DOCTYPE html>
<html lang="en">
<head>
<meta charset="utf-8">
<title>BrivaLune Mosquito Repellent Lotion – Lavender Label</title>
<link rel="stylesheet" href="https://fonts.googleapis.com/css2?family=Cinzel:wght@700;900&family=Yellowtail&display=swap">
<style>
  :root {
    --canvas: #ffffff;
    --label-fill: #2f1b4d;
    --label-border: #2b3a94;
    --label-border-inner: #3a2a6e;
    --title-yellow: #fff200;
    --shield-light: #3fc3ee;
    --shield-deep: #2a3f9c;
    --shield-edge: #f4ea1c;
    --figure-white: #ffffff;
    --insect-red: #d7141c;
    --script-white: #ffffff;
    --script-outline: #2b3a94;
  }
  html, body {
    margin: 0;
    padding: 0;
    width: 1200px;
    height: 1200px;
    overflow: hidden;
    background: var(--canvas);
  }
  .label-stage {
    position: relative;
    width: 1200px;
    height: 1200px;
  }
  .label-shape {
    position: absolute;
    left: 0;
    top: 0;
  }
  .brand-name {
    position: absolute;
    left: 0;
    width: 1200px;
    top: 300px;
    text-align: center;
    font-family: "Cinzel", serif;
    font-weight: 900;
    font-size: 62px;
    line-height: 1;
    color: var(--title-yellow);
    margin: 0;
  }
  .product-title {
    position: absolute;
    left: 0;
    width: 1200px;
    top: 420px;
    text-align: center;
    font-family: "Cinzel", serif;
    font-weight: 900;
    color: var(--title-yellow);
    margin: 0;
    line-height: 1;
  }
  .product-title .title-main {
    display: block;
    font-size: 58px;
    letter-spacing: 1px;
  }
  .product-title .title-sub {
    display: block;
    font-size: 31px;
    margin-top: 10px;
  }
  .variant-script {
    position: absolute;
    left: 0;
    top: 0;
    margin: 0;
    font-family: "Yellowtail", cursive;
    color: var(--script-white);
    -webkit-text-stroke: 1.5px var(--script-outline);
    line-height: 1;
  }
  .variant-script span {
    position: absolute;
    white-space: nowrap;
    transform-origin: left bottom;
    transform: rotate(-12deg);
  }
  .variant-script .script-with {
    left: 478px;
    top: 668px;
    font-size: 30px;
  }
  .variant-script .script-lavender {
    left: 462px;
    top: 690px;
    font-size: 64px;
  }
  .variant-script .script-fragrance {
    left: 560px;
    top: 740px;
    font-size: 64px;
  }
</style>
</head>
<body>
<main class="label-stage">
  <svg class="label-shape" width="1200" height="1200" viewBox="0 0 1200 1200">
    <defs>
      <linearGradient id="shield-gradient" x1="1" y1="0" x2="0" y2="1">
        <stop offset="0" stop-color="var(--shield-light)"/>
        <stop offset="0.35" stop-color="var(--shield-light)"/>
        <stop offset="1" stop-color="var(--shield-deep)"/>
      </linearGradient>
      <linearGradient id="figure-gradient" x1="0" y1="0" x2="0" y2="1">
        <stop offset="0" stop-color="var(--figure-white)" stop-opacity="0.95"/>
        <stop offset="1" stop-color="var(--figure-white)" stop-opacity="0.75"/>
      </linearGradient>
      <radialGradient id="insect-gradient" cx="0.5" cy="0.35" r="0.6">
        <stop offset="0" stop-color="var(--insect-red)"/>
        <stop offset="1" stop-color="var(--insect-red)" stop-opacity="0.55"/>
      </radialGradient>
    </defs>
    <path class="label-outer"
      d="M380 240 Q600 170 820 240 L820 250 Q806 600 820 980 Q820 1030 770 1030 L430 1030 Q380 1030 380 980 Q394 600 380 250 Z"
      fill="var(--label-border)"/>
    <path class="label-inner"
      d="M394 250 Q600 186 806 250 Q792 600 806 976 Q806 1016 766 1016 L434 1016 Q394 1016 394 976 Q408 600 394 250 Z"
      fill="var(--label-fill)" stroke="var(--label-border-inner)" stroke-width="3"/>
    <path class="shield-frame"
      d="M458 580 Q600 555 742 580 L742 770 Q742 870 600 935 Q458 870 458 770 Z"
      fill="var(--shield-edge)"/>
    <path class="shield-panel"
      d="M466 588 Q600 565 734 588 L734 768 Q734 862 600 925 Q466 862 466 768 Z"
      fill="url(#shield-gradient)"/>
    <rect class="figure-artwork" role="img"
      aria-label="Illustration: white silhouette of a person standing with arms raised in victory"
      x="520" y="600" width="160" height="290" rx="40"
      fill="url(#figure-gradient)"/>
    <ellipse class="mosquito-artwork" role="img"
      aria-label="Illustration: red mosquito lying defeated at the base of the shield"
      cx="600" cy="925" rx="120" ry="55"
      fill="url(#insect-gradient)"/>
  </svg>

  <p class="brand-name">BrivaLune</p>

  <h1 class="product-title">
    <span class="title-main">Mosquito</span>
    <span class="title-sub">Repellent Lotion</span>
  </h1>

  <p class="variant-script">
    <span class="script-with">with</span>
    <span class="script-lavender">Lavender</span>
    <span class="script-fragrance">Fragrance</span>
  </p>
</main>
</body>
</html>
```